Business Card Design

I need a business card for my rental business. The business is named:
Hire a Vorlatrike Brenmoor
www.hireavorlatrikebrenmoor.example
(555) 014-2937
This will be a business card that I will leave at other businesses as advertisement so it needs to have the name, website, and phone number.
Please feel free to be creative. This is a new business so I have no designs.
Thank you very much for your time and I look forward to receiving your designs
Target Market(s)
Local rental customers
Industry/Entity Type
Business
Contact Information for Business Card
Please check out my website:
Other font styles liked:
- anything creative
Colors
Designer to choose colors to be used in the design.
Requirements
Must have
- Business name, phone, website. Rentals available hourly or daily. Book online

```html
<!DOCTYPE html>
<html lang="en">
<head>
<meta charset="utf-8">
<title>Hire a Vorlatrike Brenmoor – Business Card</title>
<link rel="stylesheet" href="https://fonts.googleapis.com/css2?family=Montserrat:wght@400;500;800&display=swap">
<style>
  :root {
    --backdrop: #4e463f;
    --card-black: #161616;
    --card-sheen: #2a2a2a;
    --ink-white: #f4f4f4;
    --ink-silver: #a9adb1;
    --accent-red: #e0262b;
    --ink-soft: #d9d9d9;
  }
  * { box-sizing: border-box; margin: 0; padding: 0; }
  html, body {
    width: 1200px; height: 930px; overflow: hidden;
    background: var(--backdrop);
    font-family: "Montserrat", sans-serif;
  }
  .stage {
    position: relative; width: 1200px; height: 930px;
    display: flex; flex-direction: column; align-items: center; justify-content: center; gap: 50px;
  }
  .card {
    position: relative; width: 700px; height: 400px;
    background: linear-gradient(115deg, var(--card-black) 0%, var(--card-sheen) 45%, var(--card-black) 100%);
    box-shadow: 0 10px 24px rgba(0,0,0,0.45);
    overflow: hidden;
  }
  .card-back .brand-name {
    position: absolute; inset: 0;
    display: flex; align-items: center; justify-content: center;
    color: var(--ink-silver);
    font-weight: 800; font-size: 34px; letter-spacing: 2px; text-transform: uppercase;
  }
  .card-front .brand-name {
    position: absolute; top: 70px; left: 0; right: 0; text-align: center;
    color: var(--ink-white);
    font-weight: 800; font-size: 34px; letter-spacing: 2px; text-transform: uppercase;
  }
  .contact-row {
    position: absolute; top: 190px; left: 0; right: 0;
    display: flex; justify-content: center; align-items: center; gap: 22px;
  }
  .person { text-align: right; }
  .person-name {
    color: var(--accent-red); font-weight: 500; font-size: 28px; text-transform: uppercase; letter-spacing: 0.5px;
  }
  .person-role {
    color: var(--ink-white); font-weight: 400; font-size: 17px; text-transform: uppercase; margin-top: 4px;
  }
  .divider { width: 2px; height: 62px; background: var(--accent-red); }
  .details { color: var(--ink-white); font-size: 16px; line-height: 1.7; }
  .details .label { color: var(--accent-red); }
  .tagline {
    position: absolute; bottom: 48px; left: 0; right: 0; text-align: center;
    color: var(--ink-soft); font-size: 15px; letter-spacing: 1px; text-transform: uppercase;
  }
</style>
</head>
<body>
  <main class="stage">
    <section class="card card-back">
      <h2 class="brand-name">Hire a Vorlatrike Brenmoor</h2>
    </section>

    <section class="card card-front">
      <h1 class="brand-name">Hire a Vorlatrike Brenmoor</h1>
      <div class="contact-row">
        <div class="person">
          <p class="person-name">Darrel Quenby</p>
          <p class="person-role">Founder</p>
        </div>
        <div class="divider"></div>
        <div class="details">
          <p><span class="label">Phone:</span> (555) 014-2937</p>
          <p>www.hireavorlatrikebrenmoor.example</p>
        </div>
      </div>
      <p class="tagline">Rentals available hourly or daily-(book online)</p>
    </section>
  </main>
</body>
</html>
```